We need a DL size flyer, double sided, for our lawn mowing and gardening business, Kestrel Greens.

We want to run on the front side, the following promotion:
50% off lawn mowing, applies to first lawn mowed on any regular service,
applies to first 100 callers only, so call now!
Professional lawn mowing at an affordable price.

Logo at the bottom left, with Lawn and Garden Maintenance written just below logo.

On bottom Right contact details;
Tom and Gareth
Ph: 0487650912
Email: kestrelgreens@mailbox-example.com
www.kestrelgreens-example.com.au

Front side positioned horizontally, with a bright and colour full design in the background, with the offer of 50% Off lawn mowing in large letters along the top.

On the rear side, also positioned horizontally, a list of our services, stating;

At Kestrel Greens we specialise in the following services;
Lawn mowing
Edging
Blowing
Hedging
Pruning
Tree Loping
Weeding
Poisoning
Mulching
Fertilising
Rubbish removal
Planting
Lawn care and advice
Turf
And any other garden maintenance job,
No job too big or too small.
(No particular order, whatever fits best)
Also include our contact details,
Kestrel Greens
Ph 0487650912
www.kestrelgreens-example.com.au

Target Market(s)

Home owners, aged between 30-50 years old, moderate socio ecenomic status to more afluent areas.

Industry/Entity Type

Business

Requirements
Must have
• DL size, front and back, full colour.
Nice to have
• The writting stating "Kestrel Greens" in our logo is quite bland, if that could also be amended to make it more appealing, but change the writting design only not the actual logo.

```html
<!DOCTYPE html>
<html lang="en">
<head>
<meta charset="utf-8">
<title>Kestrel Greens – DL Flyer</title>
<link href="https://fonts.googleapis.com/css2?family=Open+Sans:wght@400;600;700;800&display=swap" rel="stylesheet">
<style>
  :root{
    --backdrop:#18243b;
    --paper:#ffffff;
    --grass-deep:#2f6e14;
    --grass-mid:#4f9a24;
    --grass-light:#8cc84a;
    --offer-red:#d8231c;
    --ink:#2a2a2a;
    --white:#ffffff;
    --accent-yellow:#f3d21c;
  }
  *{margin:0;padding:0;box-sizing:border-box;}
  html,body{width:818px;height:1200px;overflow:hidden;}
  body{background:var(--backdrop);font-family:"Open Sans",Arial,sans-serif;position:relative;}

  .flyer{position:absolute;left:60px;width:698px;background:var(--paper);overflow:hidden;}
  .flyer--front{top:112px;height:460px;}
  .flyer--back{top:628px;height:486px;}

  /* front */
  .front-grass{position:absolute;inset:0;
    background:
      linear-gradient(to top,var(--grass-deep) 0%,var(--grass-mid) 22%,rgba(95,165,49,0) 48%),
      linear-gradient(to right,var(--grass-deep) 0%,var(--grass-mid) 25%,var(--grass-light) 42%,rgba(140,200,74,0) 60%);}
  .brand{position:absolute;display:flex;align-items:center;gap:10px;}
  .brand__mark{width:30px;height:30px;background:var(--accent-yellow);}
  .brand__name{font-weight:800;font-size:26px;letter-spacing:.3px;}
  .flyer--front .brand{left:64px;top:128px;}
  .flyer--front .brand__name{color:var(--white);}

  .offer{position:absolute;left:384px;top:62px;width:290px;color:var(--offer-red);}
  .offer__percent{display:block;font-weight:800;font-size:112px;line-height:1;letter-spacing:-3px;}
  .offer__star{font-weight:700;font-size:40px;vertical-align:top;position:relative;top:6px;margin-left:4px;}
  .offer__off{display:block;text-align:right;font-weight:700;font-size:34px;line-height:1;margin:-6px 6px 0 0;}
  .offer__service{display:block;font-weight:400;font-size:37px;line-height:1.1;margin-top:4px;white-space:nowrap;}
  .offer__terms{position:absolute;left:386px;top:318px;width:290px;color:var(--white);font-size:12px;line-height:1.45;font-weight:600;}

  /* back */
  .back-grass-top{position:absolute;left:0;top:0;width:100%;height:26px;
    background:linear-gradient(to bottom,var(--grass-mid),var(--grass-light));}
  .back-grass{position:absolute;left:0;top:240px;width:100%;height:246px;
    background:linear-gradient(to bottom,var(--grass-light) 0%,var(--grass-mid) 30%,var(--grass-deep) 100%);}
  .torn-edge{position:absolute;left:0;width:100%;}
  .torn-edge--top{top:18px;height:16px;}
  .torn-edge--bottom{top:232px;height:26px;}
  .flyer--back .brand{left:46px;top:94px;}
  .flyer--back .brand__name{color:var(--grass-deep);}

  .contact{position:absolute;left:350px;top:76px;color:var(--ink);font-size:14px;line-height:1.5;font-weight:600;}

  .slogan{position:absolute;left:30px;top:318px;color:var(--white);font-weight:800;text-transform:uppercase;line-height:1.05;}
  .slogan__line{font-size:20px;}
  .slogan__big{font-size:28px;}

  .services{position:absolute;left:264px;top:300px;display:flex;color:var(--white);}
  .services__col{width:140px;padding:0 10px 0 12px;border-left:2px dotted rgba(255,255,255,.8);font-size:13px;line-height:1.35;font-weight:600;list-style:none;}
  .services__title{font-weight:800;font-size:17px;margin-bottom:2px;}
</style>
</head>
<body>

<section class="flyer flyer--front">
  <div class="front-grass" role="img" aria-label="Close-up photograph of fresh green lawn grass"></div>
  <div class="brand">
    <span class="brand__mark"></span>
    <span class="brand__name">Kestrel Greens</span>
  </div>
  <div class="offer">
    <span class="offer__percent">50%<span class="offer__star">*</span></span>
    <span class="offer__off">OFF</span>
    <span class="offer__service">LAWN MOWING</span>
  </div>
  <p class="offer__terms">*Applies to first lawn mowed on any regular service, applies to first 100 callers only, so call now!<br>Professional lawn mowing at an affordable price.</p>
</section>

<section class="flyer flyer--back">
  <div class="back-grass-top" role="img" aria-label="Strip of green lawn grass"></div>
  <svg class="torn-edge torn-edge--top" viewBox="0 0 698 16" preserveAspectRatio="none" aria-hidden="true">
    <polygon fill="#ffffff" points="0,8 30,4 60,10 95,3 130,9 170,5 210,11 250,4 290,9 330,3 370,10 410,5 450,9 490,3 530,10 570,5 610,9 650,4 698,8 698,16 0,16"/>
  </svg>
  <div class="brand">
    <span class="brand__mark"></span>
    <span class="brand__name">Kestrel Greens</span>
  </div>
  <div class="contact">
    Tom and Gareth<br>
    Ph: 0487650912<br>
    Email: kestrelgreens@mailbox-example.com<br>
    www.kestrelgreens-example.com.au
  </div>

  <div class="back-grass" role="img" aria-label="Photograph of a lush green lawn"></div>
  <svg class="torn-edge torn-edge--bottom" viewBox="0 0 698 26" preserveAspectRatio="none" aria-hidden="true">
    <polygon fill="#ffffff" points="0,0 698,0 698,14 670,20 640,10 600,18 560,8 520,16 480,6 440,15 400,9 360,20 320,11 280,17 240,7 200,16 160,10 120,19 80,8 40,15 0,10"/>
  </svg>

  <div class="slogan">
    <div class="slogan__line">No job <span class="slogan__big">too big</span></div>
    <div class="slogan__line">or too small!</div>
  </div>

  <div class="services">
    <ul class="services__col">
      <li class="services__title">SERVICES</li>
      <li>Lawn mowing</li>
      <li>Edging</li>
      <li>Blowing</li>
      <li>Hedging</li>
      <li>Pruning</li>
    </ul>
    <ul class="services__col">
      <li>Tree Loping</li>
      <li>Weeding</li>
      <li>Poisoning</li>
      <li>Mulching</li>
      <li>Fertilising</li>
      <li>Rubbish removal</li>
    </ul>
    <ul class="services__col">
      <li>Planting</li>
      <li>Lawn care and advice</li>
      <li>Turf</li>
      <li>And any other garden maintenance job</li>
    </ul>
  </div>
</section>

</body>
</html>
```